Lost & Found Website - PAYMENT GUARANTY

PC website and Mobile Website

Our website aims to develop an online management platform for lost & found objects with the use of stickers.
This solution allows users to buy stickers which will be affixed on the owners’ objects (glasses, laptops, phones …).
Users shall register the code on the website or the mobile application (flashing QR code). Platform will alert by email users if its object is found.
The person who finds an object with a sticker will be encouraged to declare the code on the web/mobile site. Once the object is found, it is identified by the system and the platform notifies the owner via email and give access to contact details of the person who found the object.

PLEASE SEE REQUIREMENT ATTACHED
Updates

Project Deadline Extended
Reason: We are waiting for more interesting ideas. Thank you all for your work. R. Delorme

Project Deadline Extended
Reason: Your designs are very next to perfection !

Target Market(s)

Our target are people 20 to 35 years old who care about there objects. Mainly French market at the beginning.

Industry/Entity Type

Management

Requirements
Must have
• Specifications:

The design must follow basic web design rules:
- Consistent site header/logo
- Page footer area includes copyright, last update, contact e-mail address
- Color scheme is limited to a maximum of three or four colors plus neutrals
- Color is used consistently
- Common fonts such as Arial or Times New Roman are used
- No more than one web font is used
- Fonts, font sizes, and font colors are consistently used
- Information is easy to find (minimal clicks)
- Find a suitable place to put the sponsor's logos.

For mobile version, we need a design that can fit to any screen size,
so please create standard mobile design.
Nice to have
• The website should allow users to:
- Create an account
- Buy lots of stickers
- Associate stickers to their objects
- Report the loss of an object by email
- Access full contact information of the finder after he paid the service
- Declare a found object
- The payment process management via Paytrov platform
Should not have
• Only PSD files.

No html.

```html
<!DOCTYPE html>
<html lang="en">
<head>
<meta charset="utf-8">
<title>Retrouvo – Home</title>
<link rel="stylesheet" href="https://fonts.googleapis.com/css2?family=Open+Sans:ital,wght@0,400;0,600;0,700;1,400;1,600;1,700&display=swap">
<style>
:root{
  --ink:#111;
  --muted:#555;
  --gold:#b8860b;
  --orange:#f28a1a;
  --orange-dark:#c9650a;
  --blue-a:#3d65a8;
  --blue-b:#27a6dd;
  --page-bg:#e3e2e0;
  --panel-bg:#ebebe9;
  --card-bg:#f4f4f4;
  --footer-bg:#f5f5f5;
  --white:#fff;
}
*{box-sizing:border-box;margin:0;padding:0}
html,body{width:1200px;height:903px;overflow:hidden}
body{font-family:"Open Sans",Arial,sans-serif;color:var(--ink);background:var(--page-bg);position:relative}
.abs{position:absolute}

/* header */
.site-header{left:0;top:0;width:1200px;height:91px;background:var(--white);box-shadow:0 2px 4px rgba(0,0,0,.18);z-index:2}
.brand{left:144px;top:20px;font-size:38px;font-weight:400;color:var(--ink);letter-spacing:.5px;line-height:50px}
.brand-dot{left:128px;top:42px;width:8px;height:8px;border-radius:50%;background:var(--ink)}
.lang{left:933px;top:13px;width:139px;height:26px;border:1px solid #d5d5d5;border-radius:3px;background:linear-gradient(#f7f7f7,#e9e9e9);font-size:11px;font-style:italic;color:#999;padding:5px 0 0 12px}
.lang-flag{right:8px;top:6px;width:22px;height:13px;background:#3c4f8c}
.main-nav{left:535px;top:53px;display:flex;align-items:center;font-size:16px;font-weight:600;line-height:22px}
.main-nav a{color:var(--ink);text-decoration:none;padding:0 16px;position:relative}
.main-nav a.current{color:var(--gold)}
.main-nav a.current::after{content:"";position:absolute;left:6px;right:6px;top:34px;height:4px;background:var(--gold)}
.nav-star{width:14px;height:14px}

/* hero */
.hero{left:0;top:91px;width:1200px;height:380px;background:radial-gradient(ellipse at 50% 35%,#f3f3f2 0%,var(--page-bg) 70%)}
.step-title{top:24px;width:320px;text-align:center;font-size:28px;font-weight:400;font-style:italic;line-height:34px;color:#2a2a2a}
.step-title.small{font-size:25px;top:26px}
.divider{top:0;width:40px;height:370px}
.step-art{border-radius:50%/40%}

/* panel */
.form-panel{left:130px;top:454px;width:939px;height:382px;background:var(--panel-bg);border-radius:8px 8px 0 0;box-shadow:0 -3px 10px rgba(0,0,0,.06)}
.card{background:var(--card-bg);border:1px solid #d9d9d9;border-radius:3px;box-shadow:0 1px 3px rgba(0,0,0,.18)}
.card-title{position:absolute;left:0;right:0;top:10px;text-align:center;font-size:21px;font-weight:700;font-style:italic;line-height:28px}
.field{position:absolute;height:33px;background:linear-gradient(#e2e2e2,#ececec);border:1px solid #cfcfcf;border-radius:2px;font-size:11px;font-style:italic;color:#666;padding:9px 0 0 11px}
.field.icon{padding-left:25px}
.field-icon{position:absolute;left:9px;top:10px;width:11px;height:12px}
.btn{position:absolute;text-align:center;border-radius:3px;box-shadow:0 2px 3px rgba(0,0,0,.3)}
.btn-orange{background:linear-gradient(#f79b2c,var(--orange) 55%,#e47b10);border:1px solid var(--orange-dark);color:#111}
.btn-submit{font-size:15px;font-weight:700;font-style:italic;padding-top:5px}
.btn-login{font-size:15px;font-weight:400;padding-top:5px}
.btn-social{color:var(--white);font-size:13px;font-weight:600;padding-top:4px;white-space:nowrap}
.btn-a{background:var(--blue-a);border:1px solid #2d4f88}
.btn-b{background:var(--blue-b);border:1px solid #1c8ab9}
.or-row{position:absolute;left:76px;width:231px;top:205px;text-align:center;font-size:14px;line-height:20px;color:#555}
.or-row::before,.or-row::after{content:"";position:absolute;top:10px;width:98px;height:1px;background:linear-gradient(90deg,transparent,#bbb,transparent)}
.or-row::before{left:0}.or-row::after{right:0}
.account-links{position:absolute;left:0;right:0;top:280px;text-align:center;font-size:13px;font-weight:600;font-style:italic;color:#555}

/* footer */
.site-footer{left:0;top:836px;width:1200px;height:67px;background:var(--footer-bg)}
.footer-nav{left:153px;top:14px;font-size:13px;color:var(--ink)}
.footer-nav span.sep{color:#bbb;margin:0 6px}
.footer-nav .current{color:var(--gold)}
.copyright{left:154px;top:37px;font-size:10.5px;color:#555}
.copyright a{font-size:13px;color:var(--ink);text-decoration:none}
.social{top:14px;width:27px;height:27px;border-radius:50%;background:#8f8f8f;border:2px solid #dcdcdc}
</style>
</head>
<body>

<header class="abs site-header">
  <div class="abs brand-dot"></div>
  <div class="abs brand">Retrouvo</div>
  <div class="abs lang">English<div class="abs lang-flag" role="img" aria-label="Language flag"></div></div>
  <nav class="abs main-nav">
    <a class="current" href="#">Home</a>
    <svg class="nav-star" viewBox="0 0 14 14"><path d="M7 0V14M0 7H14M2 2L12 12M12 2L2 12" stroke="#d4a21a" stroke-width="1.2"/></svg>
    <a href="#">Who are we?</a>
    <svg class="nav-star" viewBox="0 0 14 14"><path d="M7 0V14M0 7H14M2 2L12 12M12 2L2 12" stroke="#444" stroke-width="1.2"/></svg>
    <a href="#">How does it work?</a>
    <svg class="nav-star" viewBox="0 0 14 14"><path d="M7 0V14M0 7H14M2 2L12 12M12 2L2 12" stroke="#444" stroke-width="1.2"/></svg>
    <a href="#">Contact Us</a>
  </nav>
</header>

<section class="abs hero">
  <h2 class="abs step-title" style="left:133px">Entergistrez vos codes Retrouvo sur www.retrouvo.fr</h2>
  <h2 class="abs step-title" style="left:486px">Collez vos stickers</h2>
  <h2 class="abs step-title small" style="left:790px">Vous serez contacte’s sil’un de vos objects est retrouve</h2>

  <div class="abs step-art" style="left:150px;top:170px;width:250px;height:170px;background:radial-gradient(#d6d4d0,#e6e5e2 70%)" role="img" aria-label="Figure lying with a laptop and sticker rolls"></div>
  <div class="abs step-art" style="left:545px;top:100px;width:200px;height:240px;background:radial-gradient(#c9cbd0,#e6e5e2 70%)" role="img" aria-label="Sticker rolls, a phone, a laptop and a wallet"></div>
  <div class="abs step-art" style="left:850px;top:130px;width:210px;height:210px;background:radial-gradient(#d8d7d4,#e6e5e2 70%)" role="img" aria-label="Happy figure with a laptop, a phone and an email sign"></div>

  <svg class="abs divider" style="left:477px" viewBox="0 0 40 370"><path d="M1 0V160L30 180L1 200V370" fill="none" stroke="#c4c4c4" stroke-width="1.5"/><path d="M11 162L32 180L11 198Z" fill="#8a8a8a"/></svg>
  <svg class="abs divider" style="left:795px" viewBox="0 0 40 370"><path d="M1 0V160L30 180L1 200V370" fill="none" stroke="#c4c4c4" stroke-width="1.5"/><path d="M11 162L32 180L11 198Z" fill="#8a8a8a"/></svg>
</section>

<main class="abs form-panel"></main>

<section class="abs card" style="left:153px;top:489px;width:488px;height:319px">
  <h3 class="card-title">Have you found something?</h3>
  <div class="field" style="left:26px;top:50px;width:435px">Trouvo code :</div>
  <div class="field" style="left:26px;top:89px;width:435px">Name :</div>
  <div class="field" style="left:26px;top:128px;width:435px">Telephone :</div>
  <div class="field" style="left:26px;top:167px;width:435px">Email :</div>
  <div class="field" style="left:26px;top:206px;width:435px">Message :</div>
  <div class="btn btn-orange btn-submit" style="left:364px;top:258px;width:96px;height:33px">Submit</div>
</section>

<section class="abs card" style="left:679px;top:489px;width:368px;height:319px">
  <h3 class="card-title">Login Form</h3>
  <div class="field icon" style="left:26px;top:59px;width:314px">
    <svg class="field-icon" viewBox="0 0 11 12"><circle cx="5.5" cy="3.2" r="3" fill="#666"/><path d="M0 12C0 7.5 11 7.5 11 12Z" fill="#666"/></svg>Username</div>
  <div class="field icon" style="left:26px;top:97px;width:314px">
    <svg class="field-icon" viewBox="0 0 11 12"><path d="M3 5V3.5a2.5 2.5 0 015 0V5" fill="none" stroke="#666" stroke-width="1.6"/><rect x="1" y="5" width="9" height="7" rx="1" fill="#666"/></svg>Password</div>
  <div class="btn btn-orange btn-login" style="left:26px;top:147px;width:314px;height:34px">Login</div>
  <div class="or-row">or</div>
  <div class="btn btn-social btn-a" style="left:27px;top:234px;width:153px;height:27px">Log in with Friendbook</div>
  <div class="btn btn-social btn-b" style="left:203px;top:234px;width:137px;height:27px">Log in with Chirper</div>
  <div class="account-links">Forgot Password? &nbsp;&nbsp;|&nbsp;&nbsp; Signup</div>
</section>

<footer class="abs site-footer">
  <nav class="abs footer-nav"><span class="current">Home</span><span class="sep">/</span>Who are we?<span class="sep">/</span>How does it work?<span class="sep">/</span>Contact Us</nav>
  <p class="abs copyright">Copyright © 2013 Retrouvo.fr. All rights reserved. <a href="#">Privacy</a> <span style="color:#bbb;margin:0 5px">/</span> <a href="#">Terms of use</a></p>
  <div class="abs social" style="left:950px;background:#3b8ee8" role="img" aria-label="Social network link"></div>
  <div class="abs social" style="left:985px" role="img" aria-label="Social network link"></div>
  <div class="abs social" style="left:1019px" role="img" aria-label="Social network link"></div>
</footer>

</body>
</html>
```